Cover Page for our 2021 Comprehensive Needs Assessment Report 3 ring binder

Create a cover for our 2021 Comprehensive Needs Assessment. This is a report full of survey and non survey data, used for decision making. Modern Colors. Logo is attached as well as 2020 cover for easy explanation. However we do not want the same cover as last year, it should have a new color scheme for this year and a new look with the same feel.

Target Market(s)

School Districts

```html
<!DOCTYPE html>
<html lang="en">
<head>
<meta charset="utf-8">
<title>2021 Comprehensive Needs Assessment – Binder Cover</title>
<link href="https://fonts.googleapis.com/css2?family=Bebas+Neue&display=swap" rel="stylesheet">
<style>
  :root {
    --backdrop: #727377;
    --paper: #ffffff;
    --green-deep: #238540;
    --green-light: #4aa24a;
    --navy: #101b2b;
    --title-green: #1d8a47;
    --ink: #0a0a0a;
    --silver: #dcdcdc;
    --silver-soft: #f0f0f0;
    --logo-dot: #8cc63f;
  }
  html, body {
    margin: 0;
    width: 1200px;
    height: 1200px;
    overflow: hidden;
    background: var(--backdrop);
  }
  .cover {
    position: absolute;
    left: 362px;
    top: 264px;
    width: 476px;
    height: 673px;
    display: block;
  }
  .year, .title-line, .publisher-name {
    font-family: "Bebas Neue", "Oswald", sans-serif;
  }
  .year { fill: var(--paper); font-size: 128px; }
  .title-line { font-size: 78px; fill: var(--ink); }
  .title-line--accent { fill: var(--title-green); }
  .publisher-name { font-size: 17px; fill: var(--ink); letter-spacing: 0.4px; }
</style>
</head>
<body>
<svg class="cover" viewBox="0 0 595 841" xmlns="http://www.w3.org/2000/svg" aria-label="2021 Comprehensive Needs Assessment cover">
  <defs>
    <linearGradient id="greenField" x1="0" y1="0" x2="1" y2="1">
      <stop offset="0" stop-color="var(--green-deep)"/>
      <stop offset="0.6" stop-color="var(--green-light)"/>
    </linearGradient>
    <linearGradient id="silverBand" x1="0" y1="0" x2="0" y2="1">
      <stop offset="0" stop-color="var(--silver-soft)"/>
      <stop offset="1" stop-color="var(--silver)"/>
    </linearGradient>
  </defs>

  <rect class="paper" width="595" height="841" fill="var(--paper)"/>

  <polygon class="sheen" points="595,120 595,300 320,841 140,841" fill="var(--silver-soft)" opacity="0.7"/>
  <polygon class="sheen" points="595,560 595,700 540,841 350,841" fill="var(--silver-soft)" opacity="0.6"/>

  <polygon class="silver-band" points="470,0 500,0 75,841 18,841" fill="url(#silverBand)"/>

  <polygon class="green-field" points="0,0 457,0 0,818" fill="url(#greenField)"/>

  <polygon class="navy-wedge navy-wedge--top" points="497,0 595,0 595,45 334,292" fill="var(--navy)"/>
  <polygon class="navy-wedge navy-wedge--left" points="222,352 0,562 0,748" fill="var(--navy)"/>

  <text class="year" x="114" y="192" textLength="186" lengthAdjust="spacingAndGlyphs">2021</text>
  <rect class="year-rule" x="0" y="189" width="300" height="4" fill="var(--paper)"/>

  <text class="title-line" x="242" y="489" textLength="317" lengthAdjust="spacingAndGlyphs">COMPREHENSIVE</text>
  <text class="title-line title-line--accent" x="242" y="556" textLength="120" lengthAdjust="spacingAndGlyphs">NEEDS</text>
  <text class="title-line" x="242" y="621" textLength="253" lengthAdjust="spacingAndGlyphs">ASSESSMENT</text>

  <circle class="publisher-dot" cx="438" cy="772" r="9" fill="var(--logo-dot)"/>
  <text class="publisher-name" x="452" y="770">LEARNING</text>
  <text class="publisher-name" x="462" y="786">PATHWAYS, LLC</text>
</svg>
</body>
</html>
```